Varnek Group Business Card

Varnek Group — Business Card Design Brief
Overview
Design a double-sided business card for Varnek Group that highlights our two service arms: Varnek Communications (telecommunications) and Varnek Energy (business energy solutions). The card should feel smart and stand out when handed to clients.

Objectives
Showcase our areas of specialty clearly.
Reflect the overall Varnek / Varnek Group brand while acknowledging both arms.
Explore using both logos (Communications + Energy) or one unified logo, depending on the design.

Deliverables
One double-sided business card design (front + back).

Content & Copy
Front (preferred): Logo: Varnek / Varnek Group
Descriptor: Business Communications | Business Energy
Back:My contact details and company details
Core products: Business Mobile • Telephony • Internet • Business Energy Solutions

Brand & Visual Direction
We have a group logo currently tailored more toward telecoms, plus a separate Varnek Energy logo.
Please explore layouts that use both logos or just one, whichever works best.
Color: I wouldn't mind seeing an option using our the Blue/Purple gradient from our website (varnek-example.co.uk), but also open to non-gradient approaches and other colours..

Overall look: Smart, modern, and distinctive.
Format & Print Specs
Double-sided business card format. (Use a standard size

Must-Haves
Front: Varnek wording or Varnek Group wording with atleast 1 logo also on front “Business Communications | Business Energy.”

Back: Contact + company details and core products.
A design that stands out while remaining professional.

Nice-to-Have Options
A gradient version using our site’s Blue/Purple gradient.
A non-gradient version.
A dual-logo treatment versus a single-logo treatment.

Thanks
Dominic

```html
<!DOCTYPE html>
<html lang="en">
<head>
<meta charset="utf-8">
<title>Varnek Group Business Card</title>
<link rel="stylesheet" href="https://fonts.googleapis.com/css2?family=Montserrat:wght@400;500;700&display=swap">
<style>
  :root {
    --backdrop: #979797;
    --purple: #84449a;
    --violet: #5a55a6;
    --ocean: #0e68a8;
    --navy: #1b3562;
    --ink: #27205e;
    --white: #ffffff;
    --accent: #2aa8e0;
    --mark-green: #5cb848;
    --mark-blue: #2f6fc0;
  }
  * { box-sizing: border-box; margin: 0; padding: 0; }
  html, body {
    width: 1200px; height: 1108px; overflow: hidden;
    background: var(--backdrop);
    font-family: "Montserrat", sans-serif;
    color: var(--white);
  }
  .card {
    position: absolute; left: 242px; width: 715px; height: 408px;
    border-radius: 36px; overflow: hidden;
    background: linear-gradient(123deg,
      var(--purple) 0%, var(--purple) 38%, var(--violet) 46%,
      var(--ocean) 55%, var(--navy) 66%, var(--navy) 100%);
  }
  .card--front { top: 119px; }
  .card--back { top: 580px; }

  /* front */
  .front-mark {
    position: absolute; left: 50%; top: 48px; transform: translateX(-50%);
    width: 96px; height: 96px; border-radius: 50%; background: var(--mark-green);
  }
  .front-name {
    position: absolute; left: 0; right: 0; top: 168px; text-align: center;
    font-weight: 700; font-size: 66px; letter-spacing: 1px; color: var(--ink);
    text-transform: uppercase;
  }
  .front-descriptor {
    position: absolute; left: 0; right: 0; top: 352px; text-align: center;
    font-weight: 400; font-size: 18.5px; letter-spacing: 0.3px;
  }

  /* back */
  .back-mark {
    position: absolute; left: 50%; top: 20px; transform: translateX(-50%);
    width: 84px; height: 84px; border-radius: 50%; background: var(--mark-blue);
  }
  .back-name {
    position: absolute; left: 0; right: 0; top: 114px; text-align: center;
    font-weight: 700; color: var(--white); text-transform: uppercase; line-height: 1;
  }
  .back-name__main { display: block; font-size: 54px; letter-spacing: 1px; }
  .back-name__sub { display: block; font-size: 16px; letter-spacing: 3.6px; margin-top: 6px; }

  .person {
    position: absolute; right: calc(715px - 304px); top: 222px; text-align: right;
    white-space: nowrap;
  }
  .person__name { font-weight: 700; font-size: 33px; line-height: 1.1; }
  .person__role { font-weight: 400; font-size: 18px; margin-top: 8px; }

  .divider {
    position: absolute; left: 339px; top: 208px; width: 2px; height: 102px;
    background: var(--accent);
  }

  .contacts {
    position: absolute; left: 373px; top: 203px; list-style: none;
  }
  .contacts li {
    display: flex; align-items: center; height: 28.5px;
    font-size: 18.5px; font-weight: 400; white-space: nowrap;
  }
  .contacts svg { width: 15px; height: 15px; margin-right: 9px; flex: none; }

  .address {
    position: absolute; left: 0; right: 0; top: 330px; text-align: center;
    font-size: 17px; font-weight: 400;
  }
  .products {
    position: absolute; left: 0; right: 0; top: 362px; text-align: center;
    font-size: 16.5px; font-weight: 400; letter-spacing: 0.3px; white-space: nowrap;
  }
</style>
</head>
<body>

<section class="card card--front" aria-label="Card front">
  <div class="front-mark"></div>
  <div class="front-name">Varnek</div>
  <p class="front-descriptor">Business Communications | Business Energy</p>
</section>

<section class="card card--back" aria-label="Card back">
  <div class="back-mark"></div>
  <div class="back-name">
    <span class="back-name__main">Varnek</span>
    <span class="back-name__sub">Communications</span>
  </div>

  <div class="person">
    <p class="person__name">Adrian Kessler</p>
    <p class="person__role">Managing Director</p>
  </div>

  <div class="divider"></div>

  <ul class="contacts">
    <li>
      <svg viewBox="0 0 24 24" aria-hidden="true"><path fill="var(--accent)" d="M6.6 10.8a15.1 15.1 0 0 0 6.6 6.6l2.2-2.2c.3-.3.7-.4 1-.2 1.1.4 2.3.6 3.6.6.6 0 1 .4 1 1V20c0 .6-.4 1-1 1A17 17 0 0 1 3 4c0-.6.4-1 1-1h3.5c.6 0 1 .4 1 1 0 1.3.2 2.5.6 3.6.1.3 0 .7-.2 1z"/></svg>
      +44 0161 555 0142
    </li>
    <li>
      <svg viewBox="0 0 24 24" aria-hidden="true"><circle cx="12" cy="12" r="9" fill="none" stroke="var(--accent)" stroke-width="2.4"/></svg>
      +44 7700 900 318 (Live Chat)
    </li>
    <li>
      <svg viewBox="0 0 24 24" aria-hidden="true"><rect x="2" y="5" width="20" height="14" rx="1.5" fill="var(--accent)"/><path d="M3 6l9 7 9-7" fill="none" stroke="var(--navy)" stroke-width="1.6"/></svg>
      info@varnek-example.co.uk
    </li>
    <li>
      <svg viewBox="0 0 24 24" aria-hidden="true"><circle cx="12" cy="12" r="9.5" fill="none" stroke="var(--accent)" stroke-width="2"/><path d="M2.5 12h19M12 2.5c3 3 3 16 0 19M12 2.5c-3 3-3 16 0 19" fill="none" stroke="var(--accent)" stroke-width="1.6"/></svg>
      varnek-example.co.uk
    </li>
  </ul>

  <p class="address">24 Kestrel Row, Manchester, England, M2 7QX</p>
  <p class="products">Business Mobile • Telephony • Internet • Business Energy Solutions</p>
</section>

</body>
</html>
```